Pellridge Glassware Brand Design

Logo Design Brief

Pellridge Glassware is a startup premium drinkware company launching its first product - a premium grade 24oz Copa de Balon Gin Glass.

We are looking for branding design to produce our logo and the label for our first product; a premium 24oz Copa de Balon Gin Glass.

Design Brief for logo:

• Premium brand
• Modern, elegant and sleek design
• Not busy
• Logo does not have to include reference to drinkware

Label Design Brief:

A label design for our packaging - The packaging is tubular and will house 2 gin glasses for retail sale. The label will be stuck on the front of the tube and will need to excite people about the purchase they have just made with Pellridge Glassware.
The label design needs to incorporate the logo and reflect our premium brand image.

• The label size is 460mm x 150mm

• Label must have modern and sleek look and must not look busy.

• The label will need to work well in both multicolour and single colour print.

• Please see attached Barcode, this will need to be incorporated into the label. Barcode will need to be 300dpi or higher and 381mm x 254mm to be scannable on the packaging.

• Please see attached pictures of the tubular packaging the label is going on to

Please also see attached 3 images of the glasses being sold - This is for reference only.
Updates

Design period has been extended for 5 Days, please ensure both a logo and corresponding packaging design is submitted. Thank you Added Wednesday, October 4, 2017

Target Market(s)

Gin Drinkers - Premium - Male and Female - All ages above 18

Industry/Entity Type

It Company

Logo Text

Pellridge

Font styles to use
Serif
Sans Serif

Colors

Designer to choose colors to be used in the design.

Requirements
Must have
• Sleek modern design. Logo and Label must be submitted on this project.
Should not have
• Do not make this a busy logo or label

```html
<!DOCTYPE html>
<html lang="en">
<head>
<meta charset="utf-8">
<title>Pellridge Glassware – Gin Glass Tube Label</title>
<link rel="stylesheet" href="https://fonts.googleapis.com/css2?family=Oswald:wght@500&family=Josefin+Sans:wght@300&family=Raleway:wght@300&display=swap">
<style>
  :root {
    --backdrop: #e9e9eb;
    --label-brown: #4d2c24;
    --label-brown-deep: #3a1f19;
    --pattern-brown: #6a4438;
    --cream: #f3ece4;
    --tan: #d9c2ae;
    --tan-soft: #b89886;
  }
  * { margin: 0; padding: 0; box-sizing: border-box; }
  html, body {
    width: 1200px;
    height: 2243px;
    overflow: hidden;
    background: var(--backdrop);
  }
  .canvas {
    position: relative;
    width: 1200px;
    height: 2243px;
  }
  .label {
    position: absolute;
    left: 388px;
    top: 199px;
    width: 372px;
    height: 1822px;
    overflow: hidden;
    background: linear-gradient(90deg, var(--label-brown) 0%, var(--label-brown-deep) 55%, var(--label-brown) 100%);
  }
  .label__pattern-top {
    position: absolute;
    left: 0; top: 0;
    width: 100%;
    height: 780px;
    background: linear-gradient(180deg, var(--pattern-brown) 0%, rgba(106,68,56,0.45) 50%, rgba(106,68,56,0) 100%);
  }
  .label__pattern-side {
    position: absolute;
    top: 1180px;
    width: 70px;
    height: 642px;
    background: linear-gradient(180deg, rgba(106,68,56,0) 0%, rgba(106,68,56,0.7) 45%, var(--pattern-brown) 100%);
  }
  .label__pattern-side--left { left: 0; }
  .label__pattern-side--right { right: 0; }
  .brand {
    position: absolute;
    left: 0; top: 490px;
    width: 100%;
    text-align: center;
  }
  .brand__mark {
    display: block;
    width: 46px;
    height: 46px;
    margin: 0 auto 28px;
    border-radius: 50%;
    background: var(--tan);
  }
  .brand__name {
    font-family: "Oswald", sans-serif;
    font-weight: 500;
    font-size: 82px;
    line-height: 1;
    letter-spacing: 1px;
    color: var(--cream);
    text-transform: uppercase;
  }
  .brand__tagline {
    margin-top: 22px;
    font-family: "Josefin Sans", sans-serif;
    font-weight: 300;
    font-size: 30px;
    letter-spacing: 7px;
    color: var(--tan);
    text-transform: uppercase;
    padding-left: 7px;
  }
  .product-name {
    position: absolute;
    left: 0; top: 1218px;
    width: 100%;
    text-align: center;
    font-family: "Raleway", sans-serif;
    font-weight: 300;
    font-size: 29px;
    line-height: 55px;
    color: var(--tan);
    text-transform: uppercase;
  }
  .glass-icon {
    position: absolute;
    left: 165px;
    top: 1715px;
    width: 42px;
    height: 72px;
    border-radius: 6px;
    background: linear-gradient(180deg, var(--tan-soft), rgba(184,152,134,0.5));
  }
</style>
</head>
<body>
  <main class="canvas">
    <section class="label">
      <div class="label__pattern-top" role="img" aria-label="Fading diamond pattern across the top of the label"></div>
      <div class="label__pattern-side label__pattern-side--left" role="img" aria-label="Diamond pattern strip along the left edge"></div>
      <div class="label__pattern-side label__pattern-side--right" role="img" aria-label="Diamond pattern strip along the right edge"></div>

      <div class="brand">
        <span class="brand__mark"></span>
        <h1 class="brand__name">Pellridge</h1>
        <p class="brand__tagline">Glassware</p>
      </div>

      <p class="product-name">Premium<br>24oz<br>Copa de<br>Balon<br>Gin Glass</p>

      <div class="glass-icon" role="img" aria-label="Small gin glass icon"></div>
    </section>
  </main>
</body>
</html>
```